Singer Renmika needs a CD cover for a new song "Keep the lantern lit"

Hi. My name is Renmika. I need a CD cover for my new song "Keep the lantern lit"

I want the cover to be drawn with logos of my name and the song title only this time, so "Renmika" and "Keep the lantern lit".

My song can be heard from my website: https://renmika.sitebrook-example.com/

Those logos need to be artistic. And probably very colorful. And the logo "Renmika" is at the center. The logo "Keep lantern lit" is around it. The background is also to be artistic and colorful.

jpg file is necessary.

I would appreciate that you would challenge this for me. Thanks.

Renmika

Target Market(s)

Music industry

Colors
fbee3e

Requirements
Must have
• The logos of my name and the song title only this time, so "Renmika" and "Keep the lantern lit". The logos need to be original design.
Should not have
• Something not original product, dawn from someone's work

```html
<!DOCTYPE html>
<html lang="en">
<head>
<meta charset="utf-8">
<title>Renmika – Keep the lantern lit</title>
<link rel="stylesheet" href="https://fonts.googleapis.com/css2?family=Oswald:wght@300&family=Righteous&display=swap">
<style>
  :root {
    --gold: #fecb3b;
    --gold-edge: #5a1f12;
    --stripe: #fff6d8;
    --white: #ffffff;
    --flame: #ff8a1e;
    --ember: #e8174f;
    --dusk: #2a2f8f;
  }
  html, body {
    margin: 0;
    padding: 0;
    width: 1200px;
    height: 1200px;
    overflow: hidden;
    background: var(--dusk);
  }
  .cover {
    position: relative;
    width: 1200px;
    height: 1200px;
    overflow: hidden;
  }
  .cover__art {
    position: absolute;
    inset: 0;
    background:
      radial-gradient(circle at 42% 52%, #ffd14a 0%, var(--flame) 18%, var(--ember) 42%, transparent 66%),
      radial-gradient(circle at 85% 25%, var(--dusk) 0%, transparent 45%),
      radial-gradient(circle at 10% 85%, var(--dusk) 0%, transparent 40%),
      linear-gradient(135deg, var(--ember) 0%, #c41a6a 50%, var(--dusk) 100%);
  }
  .cover__artist {
    position: absolute;
    top: 58px;
    left: 70px;
    right: 70px;
    margin: 0;
    display: flex;
    justify-content: space-between;
    font-family: "Oswald", sans-serif;
    font-weight: 300;
    font-size: 150px;
    line-height: 1;
    color: var(--white);
  }
  .cover__title {
    position: absolute;
    inset: 0;
  }
  .cover__title text {
    font-family: "Righteous", sans-serif;
    fill: url(#title-fill);
    stroke: var(--gold-edge);
    stroke-width: 3;
    paint-order: stroke;
  }
</style>
</head>
<body>
  <main class="cover">
    <div class="cover__art" role="img" aria-label="Abstract colourful explosion of orange, red, magenta and deep blue shards bursting from the centre"></div>

    <h1 class="cover__artist" aria-label="Renmika">
      <span>R</span><span>E</span><span>N</span><span>M</span><span>I</span><span>K</span><span>A</span>
    </h1>

    <svg class="cover__title" width="1200" height="1200" viewBox="0 0 1200 1200" aria-label="Keep the lantern lit">
      <defs>
        <linearGradient id="title-fill" x1="0" y1="0" x2="0" y2="1">
          <stop offset="0" stop-color="#fecb3b"/>
          <stop offset="0.52" stop-color="#fecb3b"/>
          <stop offset="0.52" stop-color="#fff6d8"/>
          <stop offset="0.535" stop-color="#fff6d8"/>
          <stop offset="0.535" stop-color="#fecb3b"/>
          <stop offset="0.55" stop-color="#fecb3b"/>
          <stop offset="0.55" stop-color="#fff6d8"/>
          <stop offset="0.565" stop-color="#fff6d8"/>
          <stop offset="0.565" stop-color="#fecb3b"/>
          <stop offset="1" stop-color="#fecb3b"/>
        </linearGradient>
      </defs>
      <text class="cover__title-line" x="600" y="530" font-size="290" text-anchor="middle" textLength="1000" lengthAdjust="spacingAndGlyphs">keep the</text>
      <text class="cover__title-line" x="600" y="795" font-size="300" text-anchor="middle" textLength="1095" lengthAdjust="spacingAndGlyphs">lantern</text>
      <text class="cover__title-line" x="600" y="1035" font-size="290" text-anchor="middle">lit</text>
    </svg>
  </main>
</body>
</html>
```